Tidewell Recovery Business Card Design

Professional and clean design. The design colors should flow with the logo. Two-sided card with the website on the back which is:

www.TidewellRecovery.example.

"Specializing in Water Damage Restoration"

On the front I need the name, email, phone, and logo.

Name: Dorian Vashti
Email: Dorian@TidewellRecovery.example
Phone: 555-318-2046 for now

I only have the Preview and Thumbnail right now but should have the source files uploaded within a day or two.

Target Market(s)

Flood victims, home owners with water damage from busted pipes etc...

Industry/Entity Type

Business

Contact Information for Business Card

Name: Dorian Vashti

Font styles to use
Serif
Sans Serif

```html
<!DOCTYPE html>
<html lang="en">
<head>
<meta charset="utf-8">
<title>Tidewell Recovery Business Card</title>
<link rel="stylesheet" href="https://fonts.googleapis.com/css2?family=Cinzel:wght@400;600&family=Open+Sans:wght@400;600&display=swap">
<style>
  :root {
    --backdrop: #ecebe8;
    --card-white: #ffffff;
    --blue-deep: #1f7fc4;
    --blue-mid: #3aa3dc;
    --blue-light: #62c0ea;
    --blue-pale: #a7dcf3;
    --ink-grey: #6b6f74;
    --font-serif: "Cinzel", serif;
    --font-sans: "Open Sans", sans-serif;
  }
  html, body {
    margin: 0;
    width: 1200px;
    height: 800px;
    overflow: hidden;
    background: var(--backdrop);
  }
  .canvas {
    position: relative;
    width: 1200px;
    height: 800px;
  }
  .card {
    position: absolute;
    box-shadow: 0 10px 28px rgba(0,0,0,0.18);
    overflow: hidden;
  }

  /* Back of card */
  .card-back {
    left: 120px;
    top: 137px;
    width: 300px;
    height: 525px;
    background: linear-gradient(160deg, var(--blue-light) 0%, var(--blue-mid) 55%, var(--blue-deep) 100%);
    color: var(--card-white);
  }
  .card-back .brand-block {
    position: absolute;
    left: 50%;
    top: 50%;
    width: 480px;
    transform: translate(-50%, -50%) rotate(90deg);
    text-align: center;
  }
  .brand-name {
    font-family: var(--font-serif);
    font-weight: 600;
    font-size: 46px;
    letter-spacing: 3px;
    line-height: 1;
    margin: 0;
  }
  .brand-sub {
    display: flex;
    align-items: center;
    justify-content: center;
    gap: 10px;
    font-family: var(--font-serif);
    font-size: 17px;
    letter-spacing: 9px;
    margin-top: 6px;
  }
  .brand-sub::before,
  .brand-sub::after {
    content: "";
    width: 34px;
    height: 2px;
    background: currentColor;
  }
  .brand-dot {
    width: 58px;
    height: 58px;
    border-radius: 50%;
    background: var(--card-white);
    margin: 22px auto 0;
  }
  .tagline {
    position: absolute;
    left: 36px;
    top: 50%;
    width: 460px;
    margin: 0;
    transform: translate(-50%, -50%) rotate(90deg);
    font-family: var(--font-sans);
    font-size: 14px;
    text-align: center;
    white-space: nowrap;
  }

  /* Front of card */
  .card-front {
    left: 470px;
    top: 230px;
    width: 595px;
    height: 340px;
    background: var(--card-white);
  }
  .front-waves {
    position: absolute;
    inset: 0;
  }
  .front-brand {
    position: absolute;
    left: 32px;
    top: 24px;
    color: var(--blue-mid);
  }
  .front-brand .brand-name { font-size: 34px; letter-spacing: 2px; }
  .front-brand .brand-sub { font-size: 12px; letter-spacing: 7px; margin-top: 4px; }
  .front-brand .brand-sub::before,
  .front-brand .brand-sub::after { width: 26px; height: 1.5px; }

  .person {
    position: absolute;
    left: 32px;
    top: 96px;
  }
  .person-name {
    font-family: var(--font-serif);
    font-weight: 600;
    font-size: 19px;
    letter-spacing: 1px;
    color: var(--blue-mid);
    margin: 0;
  }
  .person-role {
    font-family: var(--font-sans);
    font-size: 10px;
    letter-spacing: 1px;
    color: var(--ink-grey);
    margin: 2px 0 10px;
  }
  .contact-list {
    list-style: none;
    margin: 0;
    padding: 0;
    font-family: var(--font-sans);
    font-size: 11.5px;
    color: var(--ink-grey);
  }
  .contact-list li {
    display: flex;
    align-items: center;
    gap: 8px;
    margin-bottom: 5px;
  }
  .contact-icon {
    width: 16px;
    height: 16px;
    flex: none;
  }
  .address {
    position: absolute;
    left: 24px;
    top: 248px;
    margin: 0;
    font-family: var(--font-sans);
    font-weight: 600;
    font-size: 12px;
    letter-spacing: 0.5px;
    color: var(--card-white);
    text-transform: uppercase;
    white-space: nowrap;
    transform: rotate(10deg);
    transform-origin: left center;
  }
</style>
</head>
<body>
<main class="canvas">

  <section class="card card-back" aria-label="Card back">
    <div class="brand-block">
      <p class="brand-name">TIDEWELL</p>
      <div class="brand-sub">RECOVERY</div>
      <div class="brand-dot"></div>
    </div>
    <p class="tagline">"Specializing in Water Damage Restoration"</p>
  </section>

  <section class="card card-front" aria-label="Card front">
    <svg class="front-waves" width="595" height="340" viewBox="0 0 595 340" aria-hidden="true">
      <path d="M0,222 C160,222 300,262 420,300 C500,324 560,338 595,340 L0,340 Z" fill="var(--blue-pale)"/>
      <path d="M0,262 C150,262 270,296 370,326 C410,336 450,340 480,340 L0,340 Z" fill="var(--blue-light)" opacity="0.8"/>
    </svg>

    <div class="front-brand">
      <p class="brand-name">TIDEWELL</p>
      <div class="brand-sub">RECOVERY</div>
    </div>

    <div class="person">
      <p class="person-name">DORIAN VASHTI</p>
      <p class="person-role">REALTOR</p>
      <ul class="contact-list">
        <li>
          <svg class="contact-icon" viewBox="0 0 16 16" aria-hidden="true"><circle cx="8" cy="8" r="8" fill="var(--blue-mid)"/><path d="M5.5 4.5l1.5 0 .7 2-1 .8c.5 1 1.1 1.6 2 2l.8-1 2 .7v1.5c-3.5.5-6.5-2.5-6-6z" fill="#fff"/></svg>
          555-318-2046
        </li>
        <li>
          <svg class="contact-icon" viewBox="0 0 16 16" aria-hidden="true"><circle cx="8" cy="8" r="8" fill="var(--blue-mid)"/><rect x="4" y="5" width="8" height="6" fill="none" stroke="#fff" stroke-width="1.2"/><path d="M4 5l4 3.5L12 5" fill="none" stroke="#fff" stroke-width="1.2"/></svg>
          Dorian@TidewellRecovery.example
        </li>
        <li>
          <svg class="contact-icon" viewBox="0 0 16 16" aria-hidden="true"><circle cx="8" cy="8" r="8" fill="var(--blue-mid)"/><circle cx="8" cy="8" r="4" fill="none" stroke="#fff" stroke-width="1.1"/><path d="M4 8h8M8 4c-2 2.5-2 5.5 0 8M8 4c2 2.5 2 5.5 0 8" fill="none" stroke="#fff" stroke-width="1"/></svg>
          www.TidewellRecovery.example
        </li>
      </ul>
    </div>

    <p class="address">P.O. Box: 4471 Postal Code: 208, Harbor District.</p>
  </section>

</main>
</body>
</html>
```